Website for Life Strategies business

We need a website to present our video, audio and print content to subcribers at Kindred Ascent Partners. We will offer a team of coaches who can help people breakthrough the barriers that keep them from reaching their physical, spiritual, financial, leadership and relationship goals.

Target Market(s)

Anyone who needs help with strategies to take their life to a new level of success.

Industry/Entity Type

Life Coaching

Logo Text

Kindred Ascent Partners

Number of Pages Required

5+ page

Colors

Designer to choose colors to be used in the design.

Requirements
Must have
• The ability to present content as a package that includes Word Documents, videos and audio content as well as to be able to display books for sale. Each week their would be a new package for subscribers to access. It should provide the ability for subscribers to comment on the material and share how their lives were changed by the content. Should also include a shop page to offer merchandise for sale.
Nice to have
• Not sure
Should not have
• Not sure

```html
<!DOCTYPE html>
<html lang="en">
<head>
<meta charset="utf-8">
<title>Kindred Ascent Partners — Lifestyle Strategy &amp; Coaching</title>
<link rel="stylesheet" href="https://fonts.googleapis.com/css2?family=Nunito+Sans:wght@300;400;600;700&family=Open+Sans:wght@400;600&display=swap">
<style>
:root{
  --teal:#17a8a3;
  --teal-dark:#0f8e8a;
  --orange:#ff9900;
  --orange-text:#f39a12;
  --ink:#333333;
  --muted:#8a8a8a;
  --light:#ececec;
  --white:#ffffff;
  --hero-a:#3b3a3c;
  --hero-b:#8a8580;
}
*{box-sizing:border-box;margin:0;padding:0}
html,body{width:1200px;height:2985px;overflow:hidden}
body{font-family:"Open Sans",Arial,sans-serif;color:var(--ink);background:var(--white);position:relative}
.heading{font-family:"Nunito Sans",Helvetica,sans-serif}
.abs{position:absolute}

/* hero */
.hero{left:0;top:0;width:1200px;height:653px;background:linear-gradient(135deg,var(--hero-a),var(--hero-b) 55%,#5a5755)}
.brand{left:114px;top:28px;font-family:"Nunito Sans",sans-serif;font-weight:700;font-size:29px;line-height:32px;color:var(--white)}
.brand-mark{display:inline-block;width:10px;height:10px;background:var(--orange);margin-left:8px;vertical-align:middle}
.nav-tab{left:410px;top:0;width:76px;height:6px;background:var(--orange)}
.nav{left:422px;top:46px;display:flex;gap:28px;font-family:"Nunito Sans",sans-serif;font-size:16px;color:var(--white);letter-spacing:.3px}
.hero-title{left:0;width:1200px;top:270px;text-align:center;color:var(--white)}
.hero-title h1{font-weight:400;font-size:50px;line-height:60px;letter-spacing:.5px}
.hero-title p{font-family:"Nunito Sans",sans-serif;font-size:34px;line-height:40px}
.btn-teal{display:inline-block;background:var(--teal);color:var(--white);font-size:16px;padding:10px 30px;margin-top:16px}
.dots{left:558px;top:612px;display:flex;gap:9px}
.dots span{width:14px;height:14px;border-radius:50%;background:var(--white)}
.dots span:first-child{background:transparent;border:2px solid var(--white)}

/* about */
.about-photo{left:116px;top:708px;width:464px;height:292px;background:radial-gradient(circle at 55% 55%,#ffcf55,#f08a1c 35%,#7a3a12 80%)}
.about-text{left:612px;top:716px;width:480px}
.about-text h2{font-weight:400;font-size:33px;line-height:44px;color:#333}
.about-text p{font-size:14px;line-height:24px;color:#777;margin-top:14px}
.btn-outline{display:inline-block;border:2px solid var(--orange);color:var(--orange-text);font-size:15px;padding:8px 24px;margin-top:22px}

/* videos */
.videos{left:0;top:1080px;width:1200px;height:436px;background:linear-gradient(90deg,var(--teal) 0%,#43b8b3 50%,var(--teal) 100%)}
.videos-notch{left:574px;top:1078px}
.videos h2{position:absolute;left:0;width:1200px;top:52px;text-align:center;font-weight:400;font-size:32px;color:var(--white)}
.video{top:112px;width:310px;height:216px;border:3px solid var(--white)}
.video svg{position:absolute;left:118px;top:70px}
.v1{left:116px;background:linear-gradient(180deg,#2a2a44,#5a4e6a)}
.v2{left:445px;background:linear-gradient(135deg,#3c3a3e,#a7a6a8)}
.v3{left:773px;background:radial-gradient(circle at 50% 40%,#ffd870,#e57b1a 60%,#8a4a22)}
.btn-ghost{position:absolute;left:518px;top:356px;width:172px;height:42px;border:2px solid var(--white);color:var(--white);font-size:16px;text-align:center;line-height:38px}

/* coaches */
.coach-band{left:0;top:1516px;width:1200px;height:370px}
.coach-head{left:0;width:1200px;top:1566px;text-align:center}
.coach-head h2{font-weight:400;font-size:32px;line-height:40px}
.coach-head p{font-family:"Nunito Sans",sans-serif;font-size:23px;line-height:30px}
.card{top:1672px;width:232px;height:290px;background:var(--white);box-shadow:0 2px 6px rgba(0,0,0,.15);text-align:center}
.card .photo{height:144px}
.card h3{font-weight:400;font-size:21px;margin-top:18px}
.card p{font-size:12px;line-height:18px;color:var(--muted);padding:4px 30px 0}
.btn-orange{display:inline-block;background:var(--orange);color:var(--white);font-size:11px;padding:7px 22px;margin-top:18px}
.c1{left:108px}.c1 .photo{background:linear-gradient(135deg,#1a2340,#6a5a8a,#2a3050)}
.c2{left:352px}.c2 .photo{background:linear-gradient(135deg,#c8d0d8,#5a6a80)}
.c3{left:602px}.c3 .photo{background:linear-gradient(135deg,#e2e6ea,#7e90a8)}
.c4{left:848px}.c4 .photo{background:linear-gradient(180deg,#b8b6b2,#fafaf6 55%,#444 90%)}

/* blogs */
.blogs-title{left:116px;top:2070px;font-weight:400;font-size:30px;color:var(--teal)}
.blog{top:2134px;width:298px;height:378px;background:var(--white);box-shadow:0 3px 10px rgba(0,0,0,.14)}
.blog .photo{height:200px}
.blog h3{font-family:"Nunito Sans",sans-serif;font-weight:600;font-size:17px;color:var(--orange-text);margin:22px 0 0 40px}
.blog p{font-size:13px;line-height:20px;color:var(--muted);margin:10px 30px 0 40px}
.blog .more{font-size:13px;color:#111;margin:16px 0 0 44px;display:block}
.b1{left:116px}.b1 .photo{background:linear-gradient(135deg,#3e3a38,#9c8a78)}
.b2{left:441px}.b2 .photo{background:linear-gradient(180deg,#bfae94,#e8a040 60%,#3a2a1e)}
.b3{left:766px}.b3 .photo{background:linear-gradient(180deg,#5e8a3a,#a8c070 60%,#6a7a4a)}

/* footer */
.footer{left:0;top:2586px;width:1200px;height:399px;background:var(--orange);color:var(--white)}
.col{top:64px}
.col h4{font-weight:400;font-size:17px;margin-bottom:20px}
.col li{list-style:none;font-size:13px;line-height:26px}
.input{width:262px;height:34px;border:1px solid rgba(255,255,255,.85);font-size:12px;padding-left:16px;line-height:32px;margin-bottom:10px}
.btn-submit{display:inline-block;background:var(--teal);color:var(--white);font-weight:600;font-size:15px;width:142px;height:38px;line-height:38px;text-align:center;margin-top:6px}
.socials{display:flex;gap:6px}
.socials span{width:28px;height:28px;border:1.5px solid var(--white);border-radius:50%}
.rule{left:116px;top:316px;width:968px;height:1px;background:rgba(255,255,255,.55)}
.copy{left:0;top:340px;width:1200px;text-align:center;font-size:12px}
</style>
</head>
<body>

<header class="abs hero" role="img" aria-label="Photo of a group meeting around a conference table">
</header>
<div class="abs nav-tab"></div>
<div class="abs brand">Kindred Ascent<br>Partners<span class="brand-mark"></span></div>
<nav class="abs nav"><span>HOME</span><span>ABOUT</span><span>SERVICES</span><span>VIDEO</span><span>BLOGS</span><span>WHY US</span><span>CONTACT</span></nav>
<div class="abs hero-title heading">
  <h1>Lifestyle Strategy &amp; Coaching</h1>
  <p>Morbi diam mauris viverra</p>
  <span class="btn-teal">READ MORE</span>
</div>
<div class="abs dots"><span></span><span></span><span></span><span></span></div>

<section>
  <div class="abs about-photo" role="img" aria-label="Photo of climbers helping each other up a peak at sunset"></div>
  <div class="abs about-text">
    <h2 class="heading">About Kindred Ascent Partners</h2>
    <p>Maecenas aliquet velit vel turpis Mauris neque metus malesuada nec ultricies sit amet porttitor mattis enim In massa</p>
    <p>ibero interdum nec interdum vel blandit sed ullamcorper est eget tempor cursus neque mi consectetuer mi a ultricies massa est sed nisl Class aptent taciti sociosqu ad per</p>
    <span class="btn-outline">READ MORE</span>
  </div>
</section>

<section class="abs videos">
  <h2 class="heading">Watch Our Videos</h2>
  <div class="abs video v1" role="img" aria-label="Video thumbnail of a person meditating under a starry sky"><svg width="68" height="68" viewBox="0 0 68 68"><circle cx="34" cy="34" r="32" fill="none" stroke="#fff" stroke-width="3"/><path d="M27 21 L48 34 L27 47 Z" fill="#fff"/></svg></div>
  <div class="abs video v2" role="img" aria-label="Video thumbnail of a business meeting with a laptop"><svg width="68" height="68" viewBox="0 0 68 68"><circle cx="34" cy="34" r="32" fill="none" stroke="#fff" stroke-width="3"/><path d="M27 21 L48 34 L27 47 Z" fill="#fff"/></svg></div>
  <div class="abs video v3" role="img" aria-label="Video thumbnail of a person enjoying the sunrise"><svg width="68" height="68" viewBox="0 0 68 68"><circle cx="34" cy="34" r="32" fill="none" stroke="#fff" stroke-width="3"/><path d="M27 21 L48 34 L27 47 Z" fill="#fff"/></svg></div>
  <span class="btn-ghost">VIEW MORE</span>
</section>
<svg class="abs videos-notch" width="52" height="26" viewBox="0 0 52 26"><path d="M0 0 H52 L26 24 Z" fill="#fff"/></svg>

<svg class="abs coach-band" width="1200" height="370" viewBox="0 0 1200 370"><path d="M0 0 H1200 V300 L0 370 Z" fill="var(--light)"/></svg>
<div class="abs coach-head heading">
  <h2>We will offer a Team of Coaches</h2>
  <p>who can help people in followings</p>
</div>
<article class="abs card c1"><div class="photo" role="img" aria-label="Photo of a cosmic spiritual scene"></div><h3 class="heading">Spiritual</h3><p>Praesent elementum elit at tellus Curabitur metus ipsum luctus eu malesuada</p><span class="btn-orange">READ MORE</span></article>
<article class="abs card c2"><div class="photo" role="img" aria-label="Photo of a financial presentation"></div><h3 class="heading">Financial</h3><p>Praesent elementum elit at tellus Curabitur metus ipsum luctus eu malesuada</p><span class="btn-orange">READ MORE</span></article>
<article class="abs card c3"><div class="photo" role="img" aria-label="Photo of a leader presenting to a team"></div><h3 class="heading">Leadership</h3><p>Praesent elementum elit at tellus Curabitur metus ipsum luctus eu malesuada</p><span class="btn-orange">READ MORE</span></article>
<article class="abs card c4"><div class="photo" role="img" aria-label="Photo of a person with a flag on a mountain top"></div><h3 class="heading">Relationship goals</h3><p>Praesent elementum elit at tellus Curabitur metus ipsum luctus eu malesuada</p><span class="btn-orange">READ MORE</span></article>

<h2 class="abs blogs-title heading">Latest Blogs</h2>
<article class="abs blog b1"><div class="photo" role="img" aria-label="Photo of a workshop group in discussion"></div><h3>Proin nulla arcu nonummy</h3><p>Proin nulla arcu nonummy luctus dictum eget fermentum et lorem Nunc porta convallis pedeer</p><span class="more">READ MORE</span></article>
<article class="abs blog b2"><div class="photo" role="img" aria-label="Photo of friends jumping at sunset"></div><h3>Suspendisse risus nibh</h3><p>Proin nulla arcu nonummy luctus dictum eget fermentum et lorem Nunc porta convallis</p><span class="more">READ MORE</span></article>
<article class="abs blog b3"><div class="photo" role="img" aria-label="Photo of a family walking in a park"></div><h3>Curabitur vel dolor ultrices</h3><p>Proin nulla arcu nonummy luctus dictum eget fermentum et lorem Nunc porta convallis</p><span class="more">READ MORE</span></article>

<footer class="abs footer">
  <div class="abs col" style="left:116px"><h4 class="heading">Quick Links</h4><ul><li>Home</li><li>About Us</li><li>What We Do</li><li>Why Us</li><li>Our Videos</li></ul></div>
  <div class="abs col" style="left:342px"><h4 class="heading">Resources</h4><ul><li>Our Blogs</li><li>Our Coaches</li><li>Services</li><li>Contact Us</li></ul></div>
  <div class="abs col" style="left:556px"><h4 class="heading">Newsletter Sign Up</h4><div class="input">Your Name</div><div class="input">Email address</div><span class="btn-submit">SUBMIT</span></div>
  <div class="abs col" style="left:898px"><h4 class="heading">Stay in Touch</h4><div class="socials"><span></span><span></span><span></span><span></span></div></div>
  <div class="abs rule"></div>
  <p class="abs copy">© 2017 Company Name. All right reserved. Term of Use</p>
</footer>

</body>
</html>
```